Small business services company needs a flyer designed

We need a flyer designed for a small building services company who has multiple roles ie- Roof, gutter and pressure cleaning, small building maintenance and garden cleanups. The company is based in Far North Queensland (Australia) where it is a tropical climate with lots of trees and green areas.

I want the colours to be based on the Logo and business card colours which will be added.

The flyer will need to be changeable so I can create monthly specials ie- Roof Cleaning Special, Gutter Cleaning Special or Pressure Cleaning special.

The roles of the business will be as stated on the attached business card.

Good evening all designers, please find below an update for you all, I hope it may answer some questions you have.

'd like the flyer to be DL size and at present I don't have any photo's. But i'd be happy for you to source some from google. The pictures I'd like would be of gutter cleaning from a ladder, pressure washing roofs & driveways with the large round "flat surface cleaners". Possibly have split pictures of the pressure cleaning to show before and after. 
Far North Queensland is a very tropical environment that has lots of palm trees and rain forest. The climate is usually 30+ degrees C. Incorporating those colours with the logo colours I'd like. 

Hello all designers.

I have just uploaded some of my own job pictures. There is a before and an after picture. If you source any other pictures, I'd like to see a flat surface/ spinmaster cleaner in operation, either on a roof or a driveway.

My goal is for a single sided flyer with all the details from my business card to be on the flyer. 

Please remember the climate in my area is very tropical and usually 30+ degrees C. Never cold or snowing. So please have pictures to reflect.

Thanks for the designs.
Regards,Darren

Reason: hi all designers. I have extended the deadline by 3 days to accommodate all the designers who have only recently accepted the brief nest invites. I have had a lot of declines and want the best designs I can choice from. This is no reflection of the calibre of the designs I have already received. I look forward to seeing all the updates and new designs. Regards, Darren

Home owners who take pride in the street appeal of their homes, or to add value to their selling price when a house goes on the sales market.

Building

```html
<!DOCTYPE html>
<html lang="en">
<head>
<meta charset="utf-8">
<title>Upreach Flyer</title>
<link rel="stylesheet" href="https://fonts.googleapis.com/css2?family=Arimo:wght@400;700&family=Marcellus&display=swap">
<style>
  :root{
    --brand-blue:#2b3590;
    --brand-blue-deep:#232c80;
    --brand-blue-light:#3a47a8;
    --teal:#2fc3bf;
    --white:#ffffff;
    --ink:#2b3590;
  }
  *{margin:0;padding:0;box-sizing:border-box}
  html,body{width:1200px;height:2468px;overflow:hidden;background:#fff}
  body{font-family:"Arimo",Arial,sans-serif}
  .flyer{position:relative;width:1200px;height:2468px;overflow:hidden;background:var(--white)}
  .abs{position:absolute}

  .house-photo{left:0;top:540px;width:1200px;height:540px;background:linear-gradient(180deg,#5f7a4a 0%,#7d8c78 35%,#8b8f95 55%,#c8c6b8 80%,#6d8a4c 100%)}
  .header{left:0;top:0;width:1200px;height:640px}
  .brand-name{left:76px;top:150px;font-family:"Marcellus",Georgia,serif;color:var(--white);font-size:176px;letter-spacing:4px;line-height:1;white-space:nowrap}
  .brand-tagline{left:80px;top:368px;font-family:"Marcellus",Georgia,serif;color:var(--white);font-size:27px;letter-spacing:0.5px;text-transform:uppercase;white-space:nowrap}
  .brand-call{left:240px;top:410px;font-family:"Marcellus",Georgia,serif;color:var(--white);font-size:38px;letter-spacing:2px;white-space:nowrap}

  .roof-photo{left:0;top:1080px;width:1200px;height:300px;overflow:hidden}
  .roof-before{left:0;top:0;width:1200px;height:300px;background:linear-gradient(160deg,#6e5f57 0%,#8a7a70 50%,#5b4f49 100%)}
  .photo-label{top:210px;color:var(--white);font-weight:700;font-size:64px;line-height:80px}
  .label-before{left:40px}
  .label-after{right:60px}

  .jobs-band{left:0;top:1380px;width:1200px;height:96px;background:var(--brand-blue);color:var(--white);font-weight:700;font-size:46px;text-align:center;line-height:96px;white-space:nowrap}

  .certification{left:60px;top:1520px;color:var(--teal);font-size:44px;line-height:56px;text-transform:uppercase;white-space:nowrap}
  .services-title{left:150px;top:1605px;color:var(--ink);font-weight:700;font-size:56px;line-height:70px;text-decoration:underline;text-underline-offset:8px}
  .services{left:60px;top:1685px;list-style:none}
  .services li{position:relative;padding-left:90px;color:var(--ink);font-size:50px;line-height:80px;white-space:nowrap}
  .services li::before{content:"";position:absolute;left:0;top:22px;width:36px;height:36px;background:var(--brand-blue)}

  .discount{left:0;top:2030px;width:1200px;text-align:center;color:var(--teal);font-size:46px;line-height:62px}

  .footer{left:0;top:2160px;width:1200px;height:308px}
  .contact{right:460px;top:2230px;text-align:right;font-size:40px;line-height:62px;color:var(--white);white-space:nowrap}
  .contact .abn{color:var(--teal)}
  .contact-row{display:flex;justify-content:flex-end;align-items:center;gap:18px}
  .contact-row svg{width:34px;height:34px}
  .divider{left:760px;top:2270px;width:4px;height:150px;background:var(--white)}
  .owner{left:786px;top:2278px;white-space:nowrap}
  .owner-name{color:var(--white);font-size:58px;line-height:68px}
  .owner-role{color:var(--teal);font-size:42px;line-height:50px}
</style>
</head>
<body>
<main class="flyer">

  <div class="abs house-photo" role="img" aria-label="Photo of a worker pressure cleaning the roof of a single-storey house with a ladder against the wall"></div>

  <svg class="abs header" viewBox="0 0 1200 640" aria-hidden="true">
    <defs>
      <linearGradient id="headGrad" x1="0" y1="0" x2="1" y2="1">
        <stop offset="0" stop-color="#3a47a8"/>
        <stop offset="1" stop-color="#232c80"/>
      </linearGradient>
    </defs>
    <path d="M0 0H1200V540C1000 500 820 560 600 585C380 610 180 560 0 580Z" fill="url(#headGrad)"/>
    <path d="M0 580C180 560 380 610 600 585C820 560 1000 500 1200 540" fill="none" stroke="#ffffff" stroke-width="14"/>
  </svg>

  <div class="abs brand-name">UPREACH</div>
  <div class="abs brand-tagline">Roof, Gutter &amp; Pressure Cleaning Services</div>
  <div class="abs brand-call">CALL 0400 555 123</div>

  <div class="abs roof-photo">
    <div class="abs roof-before" role="img" aria-label="Before and after photo of roof tiles, dirty on the left and cleaned on the right"></div>
    <svg class="abs" style="left:0;top:0;width:1200px;height:300px" viewBox="0 0 1200 300" aria-hidden="true">
      <path d="M600 0C700 80 760 180 820 300H1200V0Z" fill="#9a5a4a"/>
      <path d="M600 0C700 80 760 180 820 300" fill="none" stroke="#ffffff" stroke-width="8"/>
    </svg>
    <div class="abs photo-label label-before">before</div>
    <div class="abs photo-label label-after">after</div>
  </div>

  <div class="abs jobs-band">Residential, Commercial &amp; Body corporate Jobs</div>

  <div class="abs certification">National Working at Heights Certification</div>
  <div class="abs services-title">Specialized in:</div>
  <ul class="abs services">
    <li>Gutter Cleaning</li>
    <li>Pressure Cleaning-Roofs, Driveways</li>
    <li>Minor Roof, Gutter &amp; Building Maintenance</li>
    <li>Garden Waste Removal &amp; Complex Cleanup</li>
  </ul>

  <div class="abs discount">10% Discount for Emergency Services,<br>Defence &amp; Seniors</div>

  <svg class="abs footer" viewBox="0 0 1200 308" aria-hidden="true">
    <path d="M0 40C250 100 500 110 760 70C950 40 1100 0 1200 10V308H0Z" fill="var(--brand-blue)"/>
  </svg>

  <div class="abs contact">
    <div class="abn">ABN - 12 345 678 901</div>
    <div class="contact-row">0400 555 123 :
      <svg viewBox="0 0 24 24" aria-hidden="true"><path d="M6.6 10.8a15 15 0 0 0 6.6 6.6l2.2-2.2a1 1 0 0 1 1-.25 11.4 11.4 0 0 0 3.6.57 1 1 0 0 1 1 1V20a1 1 0 0 1-1 1A17 17 0 0 1 3 4a1 1 0 0 1 1-1h3.5a1 1 0 0 1 1 1c0 1.25.2 2.45.57 3.6a1 1 0 0 1-.25 1Z" fill="#2fc3bf"/></svg>
    </div>
    <div class="contact-row">roofcleaning@tropimail.com.au :
      <svg viewBox="0 0 24 24" aria-hidden="true"><rect x="2" y="5" width="20" height="14" fill="none" stroke="#2fc3bf" stroke-width="2"/><path d="M2 5l10 8 10-8" fill="none" stroke="#2fc3bf" stroke-width="2"/></svg>
    </div>
  </div>
  <div class="abs divider"></div>
  <div class="abs owner">
    <div class="owner-name">Darren Calder</div>
    <div class="owner-role">owner operator</div>
  </div>

</main>
</body>
</html>
```